Customizable Gift Note Card Design

I need a gift note card designed for my Healthy Snacks Care Package company. I need to be able to customize each card with the customer's gift message to the recipient and print to a standard printer.

The card should be single-sided 5 x 7, include our logo, keep colors and graphics simple since they will be printed for each individual order on a standard printer. I would like the following quote to be included in a small and subtle way: "Food is symbolic of love when words are inadequate." —Brent K. Hollister. Our website themerrypantrybites.com should also be included.

I have included pictures of our product packaging for reference.

Target Market(s)

Gift recipients: Students, people recovering from illness, housewarming, thank you gifts...etc.

Industry/Entity Type

It Company

Colors

Designer to choose colors to be used in the design.

Requirements
Must have
• We are looking for a simple, cute and elegant gift card that reflects our branding. Must be customizable and printable on a standard printer.
• Must be single-sided 5x7.

```html
<!DOCTYPE html>
<html lang="en">
<head>
<meta charset="utf-8">
<title>The Merry Pantry – Gift Note Card</title>
<link rel="stylesheet" href="https://fonts.googleapis.com/css2?family=Yellowtail&family=Montserrat:wght@400;500&display=swap">
<style>
  :root {
    --paper: #f3f0e8;
    --paper-wash: #e6e0d2;
    --gold: #c99a1c;
    --gold-light: #f1d36a;
    --ink: #1a1a1a;
    --berry: #a3141f;
    --grey-mark: #cfcfcf;
    --ring: #e4efcc;
    --rose-line: #f0a9ad;
  }
  * { box-sizing: border-box; margin: 0; padding: 0; }
  html, body { width: 931px; height: 1200px; overflow: hidden; background: #ffffff; }
  .card {
    position: relative; width: 931px; height: 1200px;
    background: radial-gradient(ellipse at 50% 45%, var(--paper-wash) 0%, var(--paper) 55%, #fbfaf6 100%);
    font-family: "Montserrat", sans-serif; color: var(--ink);
  }
  .foil { position: absolute; top: 0; height: 240px; width: 260px; }
  .foil--left { left: 0; background: linear-gradient(160deg, var(--gold-light), var(--gold) 45%, transparent 75%); }
  .foil--right { right: 0; background: linear-gradient(200deg, var(--gold-light), var(--gold) 45%, transparent 75%); }
  .frame { position: absolute; inset: 70px 28px 28px 28px; border: 2px solid var(--gold); }
  .mascot {
    position: absolute; left: 340px; top: 70px; width: 250px; height: 290px;
    background: radial-gradient(ellipse at center, #3a3a3a 0%, #2a2a2a 40%, rgba(120,20,30,0.35) 65%, transparent 72%);
  }
  .quote { position: absolute; left: 0; width: 931px; top: 400px; text-align: center; font-family: "Yellowtail", cursive; transform: rotate(-5deg); }
  .quote__line { display: block; line-height: 1; text-shadow: 2px 3px 3px rgba(0,0,0,0.2); }
  .quote__line--one { font-size: 62px; }
  .quote__line--two { font-size: 62px; margin-top: 10px; }
  .quote__line--three { font-size: 58px; margin-top: 18px; }
  .accent { color: var(--berry); font-size: 96px; }
  .quote__author { position: absolute; left: 460px; top: 690px; font-family: "Yellowtail", cursive; font-size: 40px; color: var(--berry); transform: rotate(-5deg); }
  .brand-mark { position: absolute; left: 60px; top: 820px; width: 180px; height: 180px; border-radius: 50%; background: #fafafa; border: 10px solid var(--ring); }
  .brand { position: absolute; left: 310px; top: 835px; transform: rotate(-4deg); }
  .brand__name { font-family: "Yellowtail", cursive; font-size: 64px; color: var(--ink); line-height: 1; }
  .brand__web { margin-top: 14px; margin-left: 30px; font-size: 19px; font-weight: 500; color: var(--berry); }
  .note {
    position: absolute; left: 62px; top: 1000px; width: 810px; height: 150px;
    border: 2px solid var(--rose-line); border-radius: 18px; background: rgba(255,255,255,0.85);
    transform: rotate(-2deg); padding: 42px 40px 0 50px; font-size: 19px;
  }
  .note__row { display: flex; align-items: baseline; margin-bottom: 38px; }
  .note__label { width: 66px; }
  .note__line { flex: 1; border-bottom: 2px dotted #555; }
</style>
</head>
<body>
  <main class="card">
    <div class="foil foil--left" role="img" aria-label="Gold foil brush stroke decoration"></div>
    <div class="foil foil--right" role="img" aria-label="Gold foil brush stroke decoration"></div>
    <div class="frame"></div>
    <div class="mascot" role="img" aria-label="Illustration of a gentleman with bowler hat, red glasses, moustache and bow tie"></div>
    <p class="quote">
      <span class="quote__line quote__line--one"><span class="accent">Food</span> is symbolic</span>
      <span class="quote__line quote__line--two">of <span class="accent">Love</span></span>
      <span class="quote__line quote__line--three">when words are inadequate</span>
    </p>
    <p class="quote__author">- Brent K. Hollister</p>
    <div class="brand-mark"></div>
    <div class="brand">
      <p class="brand__name">The Merry Pantry</p>
      <p class="brand__web">www.themerrypantrybites.com</p>
    </div>
    <section class="note">
      <div class="note__row"><span class="note__label">To</span><span class="note__line"></span></div>
      <div class="note__row"><span class="note__label">From</span><span class="note__line"></span></div>
    </section>
  </main>
</body>
</html>
```